Brindle Financial Advice - Employer Benefit Brochure

We need to design a professional looking brochure that we can present to our existing client base, and assist in attracting new clients.
The current information is just provided in a word document, but we need to improve significantly.
The audience would be business leaders, HR decision makers and member policy committee members

Industry/Entity Type

Business

Font styles to use
Sans Serif

Colors
0255a3
f37122

```html
<!DOCTYPE html>
<html lang="en">
<head>
<meta charset="utf-8">
<title>Brindle Financial Advice – Employer Benefits Brochure</title>
<link href="https://fonts.googleapis.com/css2?family=Source+Sans+3:ital,wght@0,400;0,600;0,700;1,400&display=swap" rel="stylesheet">
<style>
:root{
  --blue:#2a51a7;
  --blue-dark:#2148a0;
  --orange:#f15a22;
  --white:#ffffff;
  --sky-top:#5f8fd0;
  --sky-bottom:#dfe8f3;
}
*{margin:0;padding:0;box-sizing:border-box}
html,body{width:1200px;height:994px;overflow:hidden;background:var(--white)}
body{font-family:"Source Sans 3",sans-serif;position:relative}
.block{position:absolute}
.about-panel{left:107px;top:115px;width:330px;height:768px;background:var(--blue)}
.base-band{left:437px;top:460px;width:664px;height:423px;background:var(--blue)}
.employer-panel{left:437px;top:243px;width:328px;height:437px;background:var(--orange)}
.fee-box{left:437px;top:680px;width:328px;height:105px;background:var(--white)}
.fee-tail{left:523px;top:780px;width:242px;height:77px;background:var(--white)}
.signpost-photo{left:765px;top:272px;width:336px;height:188px;background:linear-gradient(180deg,var(--sky-top),var(--sky-bottom))}

.about{left:107px;top:190px;width:330px;text-align:center;color:var(--orange)}
.about h2{color:var(--white);font-weight:700;font-size:27px;margin-bottom:10px}
.about h3{color:var(--white);font-weight:600;font-size:17px;margin:0 0 14px}
.about p{font-size:12.6px;line-height:16.6px;padding:0 26px}
.about .lead{font-style:italic}
.about .gap{margin-bottom:30px}

.headline{left:493px;top:162px;color:var(--blue);font-size:43px;font-weight:400;letter-spacing:-.5px;line-height:1}
.headline-accent{left:783px;top:206px;color:var(--orange);font-size:49px;font-weight:400;line-height:1}

.employer{left:460px;top:248px;width:282px;color:var(--white)}
.employer .t1{color:var(--blue);font-size:20px;font-weight:700;line-height:1}
.employer .t2{font-size:20px;margin-left:58px;line-height:1}
.employer .core{color:var(--blue);font-size:13px;font-weight:700;text-align:right;margin-top:1px}
.employer h4{color:var(--blue);font-size:13px;font-weight:700;text-align:center;margin:6px 0 4px}
.employer p{font-size:9.6px;line-height:12.8px;text-align:justify;text-align-last:center}
.services{display:grid;grid-template-columns:1fr 1fr;font-size:9.6px;line-height:12.8px;text-align:center}

.fee{left:452px;top:684px;width:298px;color:var(--blue)}
.fee h4{font-size:16px;font-weight:700;text-align:center;margin-bottom:3px}
.fee p{font-size:11.4px;line-height:15.3px;text-align:justify;text-align-last:center}

.employee{left:788px;top:476px;width:262px;color:var(--orange)}
.employee .t1{color:var(--white);font-size:20px;font-weight:600;line-height:1}
.employee .t2{font-size:21px;margin-left:66px;line-height:1.2}
.employee .core{color:var(--white);font-size:14px;font-weight:600;margin:6px 0 0 18px}
.employee h4{color:var(--white);font-size:12.5px;font-weight:600;text-align:center;margin:1px 0 6px}
.employee p{font-size:9.2px;line-height:12.7px;text-align:justify;text-align-last:center;margin-left:18px}
.employee ul{list-style:none;font-size:9.2px;line-height:12.8px;text-align:center;margin-left:18px}
</style>
</head>
<body>
<div class="block about-panel"></div>
<div class="block base-band"></div>
<div class="block employer-panel"></div>
<div class="block fee-box"></div>
<div class="block fee-tail"></div>
<div class="block signpost-photo" role="img" aria-label="Photo of a signpost against blue sky with signs reading Support, Help, Advice, Assistance and Guidance"></div>

<section class="block about">
  <h2>ABOUT US</h2>
  <p class="lead">Brindle Financial Advice Group has been based in North Sydney since 1983 and has over 30 years of practical financial planning experience. Our long-term success has been achieved through the building of strong relationships and mutual trust over many years of providing quality advice services to our corporate and private clients and their families.</p>
  <p class="lead" style="margin-top:17px" class="gap">We provide an integrated Employer Benefits Program with solutions in superannuation, wealth and risk management and debt advice, with a focus on both business and personal financial planning.</p>
  <h3 style="margin-top:32px">VISION</h3>
  <p>To operate a unique, superior &amp;<br>profitable financial services business.</p>
  <h3 style="margin-top:26px">MISSION</h3>
  <p>To focus on our clients and exceed their expectations by providing a professional, high quality client experience with the emphasis on Integrated Financial Services and Employer Benefit Solutions for businesses, individuals and families.</p>
  <h3 style="margin-top:26px">VALUES</h3>
  <p>Honesty, Integrity, Empathy,<br>Passion, Persistence,<br>Accountability.&nbsp; Fun</p>
</section>

<h1 class="block headline">MAKING THE PIECES FIT</h1>
<div class="block headline-accent">TOGETHER</div>

<section class="block employer">
  <div class="t1">EMPLOYER</div>
  <div class="t2">BENEFITS PROGRAM</div>
  <div class="core">CORE SERVICES</div>
  <h4 style="margin-top:3px">Corporate Superannuation Services</h4>
  <p>Superannuation is a long-term investment so it's crucial to have the right partner who will consistently deliver outstanding support to you and your employees. Brindle has an extensive knowledge of superannuation providers in the market and can ensure that you have the right solution for your long-term business requirements.</p>
  <h4>Insurance Services</h4>
  <p>The right insurance plan provides you and your employees with peace of mind and security in the event of an accident, injury or illness. In our experience, taking insurance cover through the corporate superannuation plan is most cost effective and efficient solution.&nbsp; However, the option to take Group Salary Continuance outside of superannuation has a number of benefits and should also be considered.</p>
  <h4>Financial Literacy &amp; Education Program</h4>
  <p>We believe that educating your employees on a range of topics not only increases their awareness of financial solutions, but helps them cut through the noise, make more informed choices and take control of their financial future.</p>
  <h4>Additional Corporate Services</h4>
  <div class="services">
    <span>Health Insurance</span><span>General &amp; Business Insurance</span>
    <span>Travel Insurance</span><span>Outplacement Solutions</span>
    <span>Key Person Insurance</span><span>Professional Contractor</span>
    <span>Asset &amp; Equipment Finance</span><span>Network</span>
  </div>
</section>

<section class="block fee">
  <h4>FEE FLEXIBILITY</h4>
  <p>The objective of our fee structure is to offer our clients flexible fee solutions that are tailored to the needs of the group, relate to the value delivered and are mutually beneficial.&nbsp; On completion of a full scope of works we will quote and discuss the fee specific to your business.</p>
</section>

<section class="block employee">
  <div class="t1">EMPLOYEE</div>
  <div class="t2">BENEFITS PROGRAM</div>
  <div class="core">CORE SERVICES</div>
  <h4 style="margin-left:18px">Superannuation Advice Services</h4>
  <p>As part of our initial engagement, we encourage all members of the superannuation plan to make more informed and active choices in regards to their investment asset allocation and portfolio selection. Encouraging employees to become engaged in all aspects of their superannuation will lead to a secure financial future and fulfilling retirement.</p>
  <h4 style="margin:3px 0 3px 18px">Insurance Advice Services</h4>
  <p>As part of our initial engagement, we ensure that all members who have automatic insurance cover within the superannuation plan review their levels of cover. It's important that the cover is at an appropriate level for their individual needs.</p>
  <h4 style="margin:8px 0 3px 18px">Additional Employee Services</h4>
  <ul>
    <li>Financial Planning</li>
    <li>Wills &amp; Estate Planning</li>
    <li>Trauma (Critical Illness) Insurance</li>
    <li>Home &amp; Investment Lending</li>
    <li>Property Advice</li>
    <li>Car Leasing Finance</li>
  </ul>
</section>
</body>
</html>
```